Velmar Corsa 340 mid roof wrap for remodeling company

I think most car wraps are tacky. I want to keep it simple and clean. No full wraps, it should be a partial wrap, and I want the main color to be white.

Black and white is best, but if adding one or two more colors would work best, we can do that. Gray would be the first choice, and maybe one more like red or blue if needed.

I included a photo of the blank van photos with my logos superimposed in the way I have them on my current vehicle. I do want to keep the same fonts, info, and arrow logo.

```html
<!DOCTYPE html>
<html lang="en">
<head>
<meta charset="utf-8">
<title>Northvale Homes – Velmar Corsa 340 Partial Wrap</title>
<link href="https://fonts.googleapis.com/css2?family=Montserrat:wght@500;600&family=Poppins:wght@400;600&display=swap" rel="stylesheet">
<style>
  :root {
    --canvas: #ffffff;
    --body-white: #fbfbfb;
    --panel-edge: #d6d6d6;
    --ink: #111111;
    --mark-gray: #6e6e6e;
    --stripe-dark: #3a3a3a;
    --stripe-light: #9a9a9a;
    --photo-warm: #8a5a36;
    --photo-light: #d9cfc4;
    --sketch-light: #f3f3f3;
    --sketch-mid: #dadada;
  }
  html, body {
    margin: 0;
    width: 1200px;
    height: 1200px;
    overflow: hidden;
    background: var(--canvas);
  }
  .wrap-sheet {
    width: 1200px;
    height: 1200px;
    display: flex;
    flex-direction: column;
    justify-content: center;
    gap: 80px;
    align-items: center;
  }
  .wrap-side {
    width: 1100px;
    height: 470px;
    display: block;
  }
  .brand-name {
    font-family: "Montserrat", sans-serif;
    font-weight: 600;
    font-size: 30px;
    fill: var(--ink);
  }
  .brand-sub {
    font-family: "Montserrat", sans-serif;
    font-weight: 500;
    font-size: 22px;
    fill: var(--ink);
  }
  .phone {
    font-family: "Poppins", sans-serif;
    font-weight: 600;
    font-size: 30px;
    fill: var(--ink);
  }
  .website {
    font-family: "Poppins", sans-serif;
    font-weight: 400;
    font-size: 15.5px;
    fill: var(--ink);
  }
  .license {
    font-family: "Poppins", sans-serif;
    font-weight: 400;
    font-size: 11.5px;
    fill: #333333;
  }
</style>
</head>
<body>
<main class="wrap-sheet">

  <svg class="wrap-side wrap-side--photo" viewBox="0 0 1100 470" xmlns="http://www.w3.org/2000/svg">
    <defs>
      <linearGradient id="stripeGrad" x1="0" y1="0" x2="0" y2="1">
        <stop offset="0" stop-color="var(--stripe-dark)"/>
        <stop offset="1" stop-color="var(--stripe-light)"/>
      </linearGradient>
      <linearGradient id="photoGrad" x1="0" y1="0" x2="1" y2="1">
        <stop offset="0" stop-color="var(--photo-warm)"/>
        <stop offset="0.55" stop-color="#b08a6a"/>
        <stop offset="1" stop-color="var(--photo-light)"/>
      </linearGradient>
    </defs>
    <rect class="body-panel" x="4" y="4" width="1092" height="462" rx="30" fill="var(--body-white)" stroke="var(--panel-edge)" stroke-width="2"/>
    <polygon class="accent-stripe" points="843,4 870,4 722,466 695,466" fill="url(#stripeGrad)"/>
    <path class="kitchen-photo" role="img" aria-label="Photo of a remodeled kitchen with white cabinets, dark countertops and stainless appliances"
          d="M882,4 H1066 A30,30 0 0 1 1096,34 V436 A30,30 0 0 1 1066,466 H734 Z" fill="url(#photoGrad)"/>
    <rect class="brand-mark" x="530" y="40" width="70" height="70" fill="var(--mark-gray)"/>
    <text class="brand-name" x="565" y="186" text-anchor="middle" textLength="285" lengthAdjust="spacing">NORTHVALE</text>
    <text class="brand-sub" x="565" y="220" text-anchor="middle" textLength="153" lengthAdjust="spacing">HOMES</text>
    <text class="license" x="230" y="274" textLength="150" lengthAdjust="spacing">LICENSE #HIC.0571284</text>
    <text class="phone" x="565" y="268" text-anchor="middle" textLength="247" lengthAdjust="spacingAndGlyphs">(555) 214-0386</text>
    <text class="website" x="565" y="294" text-anchor="middle" textLength="220" lengthAdjust="spacing">www.northvalehomesct.com</text>
  </svg>

  <svg class="wrap-side wrap-side--sketch" viewBox="0 0 1100 470" xmlns="http://www.w3.org/2000/svg">
    <defs>
      <linearGradient id="sketchGrad" x1="0" y1="0" x2="1" y2="0">
        <stop offset="0" stop-color="var(--body-white)"/>
        <stop offset="0.3" stop-color="var(--sketch-light)"/>
        <stop offset="1" stop-color="var(--sketch-mid)"/>
      </linearGradient>
    </defs>
    <rect class="body-panel" x="4" y="4" width="1092" height="462" rx="30" fill="var(--body-white)" stroke="var(--panel-edge)" stroke-width="2"/>
    <path class="kitchen-sketch" role="img" aria-label="Architectural line sketch of a kitchen with island and bar stools in perspective"
          d="M740,4 H1066 A30,30 0 0 1 1096,34 V436 A30,30 0 0 1 1066,466 H740 Z" fill="url(#sketchGrad)"/>
    <rect class="brand-mark" x="530" y="40" width="70" height="70" fill="var(--mark-gray)"/>
    <text class="brand-name" x="565" y="186" text-anchor="middle" textLength="285" lengthAdjust="spacing">NORTHVALE</text>
    <text class="brand-sub" x="565" y="220" text-anchor="middle" textLength="153" lengthAdjust="spacing">HOMES</text>
    <text class="license" x="230" y="274" textLength="150" lengthAdjust="spacing">LICENSE #HIC.0571284</text>
    <text class="phone" x="565" y="268" text-anchor="middle" textLength="247" lengthAdjust="spacingAndGlyphs">(555) 214-0386</text>
    <text class="website" x="565" y="294" text-anchor="middle" textLength="220" lengthAdjust="spacing">www.northvalehomesct.com</text>
  </svg>

</main>
</body>
</html>
```